Commercial Real Estate

We need a business card design for a new commercial real estate business that specializes in apartment building brokerage. Not individual units but the entire complex. We find and represent the owners existing buildings and well as new buyers for those buildings. The design should convey trust, integrity, knowledge and growth. It should be easily read.

Target Market(s)

40 to 65 years old

Industry/Entity Type

Real Estate

```html
<!DOCTYPE html>
<html lang="en">
<head>
<meta charset="utf-8">
<title>Valmora – Business Card</title>
<link href="https://fonts.googleapis.com/css2?family=Open+Sans:wght@400;700&display=swap" rel="stylesheet">
<style>
  :root {
    --backdrop: #e9eaeb;
    --card: #f7f7f6;
    --teal: #4fb3b3;
    --ink: #4a5656;
    --divider: #dcdddc;
  }
  * { margin: 0; padding: 0; box-sizing: border-box; }
  html, body {
    width: 1200px; height: 720px; overflow: hidden;
    background: var(--backdrop);
    font-family: "Open Sans", Verdana, sans-serif;
  }
  .card {
    position: absolute; left: 75px; top: 60px;
    width: 1050px; height: 600px;
    background: var(--card);
    box-shadow: 0 10px 30px rgba(0,0,0,0.08);
    display: flex;
  }
  .brand-panel {
    width: 420px; height: 100%;
    border-right: 1px solid var(--divider);
    display: flex; align-items: center; justify-content: center;
    gap: 18px;
  }
  .brand-mark {
    width: 26px; height: 26px; background: var(--teal);
  }
  .brand-name {
    font-size: 52px; font-weight: 700; color: var(--ink);
    letter-spacing: 4px;
  }
  .contact-panel {
    flex: 1; padding: 70px 0 0 70px; color: var(--ink);
  }
  .person-name {
    font-size: 44px; font-weight: 700; color: var(--teal);
    letter-spacing: 1px; line-height: 1.1;
  }
  .person-title { font-size: 30px; line-height: 1.2; }
  .address { margin-top: 44px; font-size: 30px; line-height: 1.25; }
  .channels { margin-top: 34px; list-style: none; font-size: 30px; line-height: 1.35; }
  .channels li { display: flex; align-items: center; gap: 16px; }
  .channels svg { width: 28px; height: 28px; flex: none; }
  .accent { color: var(--teal); }
</style>
</head>
<body>
  <div class="card">
    <div class="brand-panel">
      <span class="brand-mark"></span>
      <span class="brand-name">VALMORA</span>
    </div>
    <div class="contact-panel">
      <p class="person-name">DANIEL REED</p>
      <p class="person-title">Managing Director</p>
      <p class="address">PO. BOX 1000<br>Land dummy<br>dummy dummy City</p>
      <ul class="channels">
        <li>
          <svg viewBox="0 0 24 24" aria-hidden="true"><path fill="var(--teal)" d="M3 6c0-2 2-3 9-3s9 1 9 3v2h-5V6.5c-1-.5-7-.5-8 0V8H3zM6 9h12l2 10H4zM10 12v4h4v-4z"/></svg>
          <span>00 00 00 00 00</span>
        </li>
        <li>
          <svg viewBox="0 0 24 24" aria-hidden="true"><rect x="2" y="5" width="20" height="14" fill="var(--teal)"/><path d="M2 5l10 8 10-8" fill="none" stroke="#fff" stroke-width="1.6"/></svg>
          <span>daniel@valmora.com</span>
        </li>
        <li>
          <svg viewBox="0 0 24 24" aria-hidden="true"><circle cx="12" cy="12" r="9" fill="none" stroke="var(--teal)" stroke-width="2"/><path d="M3 12h18M12 3c4 4 4 14 0 18M12 3c-4 4-4 14 0 18" fill="none" stroke="var(--teal)" stroke-width="1.5"/></svg>
          <span>www.<span class="accent">valmora</span>.com</span>
        </li>
      </ul>
    </div>
  </div>
</body>
</html>
```